Website Revamp: Vormesh.com

Just got a new logo looking for a web design to go with the business. I need the photoshop files and stock photos. No Word Press Please.

```html
<!DOCTYPE html>
<html lang="en">
<head>
<meta charset="utf-8">
<title>Vormesh – Auto Recycling</title>
<link rel="stylesheet" href="https://fonts.googleapis.com/css2?family=Raleway:wght@400;500;600;700;800&display=swap">
<style>
:root{
  --dark:#2b2b2b;
  --dark-2:#2f2f30;
  --card:#2a2a2b;
  --green:#8cc63f;
  --green-deep:#7cb83a;
  --text:#222;
  --muted:#7a7a7a;
  --line:#c9c9c9;
  --white:#fff;
}
*{box-sizing:border-box;margin:0;padding:0}
html,body{width:1200px;height:4751px;overflow:hidden}
body{position:relative;background:var(--white);font-family:"Raleway",sans-serif;color:var(--text)}
.abs{position:absolute}
.center{left:0;width:1200px;text-align:center}

/* header */
.site-header{left:0;top:0;width:1200px;height:127px;background:var(--dark)}
.call{left:112px;top:20px;color:#ddd;font-size:13px;display:flex;align-items:center;gap:10px}
.call b{font-size:20px;font-weight:500;color:#fff}
.social-top{left:1016px;top:22px;display:flex;gap:10px}
.social-top span{width:12px;height:12px;border-radius:50%;border:1.5px solid #fff;display:block}
.nav{top:80px;font-size:14px;font-weight:500;color:#fff;letter-spacing:.3px}
.nav.active{color:var(--green)}
.brand{left:540px;top:14px;width:120px;text-align:center;color:#fff}
.brand .mark{width:54px;height:54px;border-radius:50%;border:2px solid #fff;margin:0 auto 6px}
.brand .name{font-size:17px;font-weight:800;letter-spacing:1px}

/* hero */
.hero{left:0;top:127px}
.hero-title{top:280px;font-size:92px;font-weight:800;color:#fff;letter-spacing:2px}
.hero-sub{top:394px;font-size:19px;line-height:33px;color:#fff;font-weight:500}
.btn{display:flex;align-items:center;justify-content:center;background:var(--green);color:#fff;font-size:13px;font-weight:500;border-radius:3px}
.dot{width:12px;height:12px;border-radius:50%;background:#fff}
.dot.on{background:var(--green);border:2px solid #fff}

/* about */
.photo{display:block}
.frame{left:829px;top:955px;width:238px;height:392px;border:3px solid #444;border-left:none}
.h2{font-size:40px;font-weight:700;color:var(--text)}
.para{font-size:14px;line-height:34px;color:var(--muted);text-align:justify}

/* services */
.band-dark{left:0;width:1200px;background:var(--dark-2)}
.band-title{font-size:40px;font-weight:700;color:#fff}
.service{top:1646px;width:318px;height:439px;background:var(--card);text-align:center;color:#fff;box-shadow:0 2px 6px rgba(0,0,0,.25)}
.service .img{width:100%;height:216px}
.service h3{margin-top:46px;font-size:19px;font-weight:500}
.service p{margin:14px 10px 0;font-size:13px;line-height:26px;color:#ddd}
.service a{display:inline-block;margin-top:12px;color:var(--green);font-size:16px;font-weight:500;text-decoration:underline}
.chev{width:20px;height:30px}

/* benefits */
.benefits{left:0;top:2634px;width:1200px;height:472px}
.benefits-text{left:130px;top:2847px;width:940px;text-align:center;font-size:15px;line-height:34px;color:#fff}

/* blogs */
.blog{top:3332px;width:318px;height:254px;color:#fff}
.blog .cap{position:absolute;left:18px;font-size:13px;line-height:25px;font-weight:500}
.blog .date{font-size:12px}
.blog .more{font-size:13px;text-decoration:underline}

/* contact */
.band-green{left:0;top:3695px;width:1200px;height:127px;background:var(--green)}
.field{border:1.5px solid var(--line);font-size:15px;color:#777;padding:14px 14px}
.send{left:610px;top:4187px;width:363px;height:48px;background:#4b4b4c;color:#fff;font-size:16px;font-weight:600;display:flex;align-items:center;justify-content:center}

/* footer */
.site-footer{left:0;top:4335px;width:1200px;height:416px;background:#2a2a2a}
.f-head{top:4396px;font-size:14px;font-weight:600;color:#fff}
.f-list{top:4438px;list-style:none;font-size:14px;color:#d9d9d9;line-height:34.5px}
.f-icon{width:38px;height:38px;border-radius:50%;border:1.5px solid #fff;display:flex;align-items:center;justify-content:center}
.f-txt{font-size:14px;color:#e6e6e6;line-height:25px}
.s-row{left:944px;display:flex;align-items:center;gap:10px;font-size:14px;color:#d9d9d9}
.s-row span{width:32px;height:32px;border-radius:50%;border:1.5px solid #fff}
.rule{left:112px;top:4682px;width:976px;height:1px;background:#444}
.copy{top:4706px;font-size:14px;color:#d9d9d9}
</style>
</head>
<body>

<header class="abs site-header">
  <div class="abs call">
    <svg width="18" height="18" viewBox="0 0 24 24" fill="none" stroke="#ddd" stroke-width="1.6"><path d="M5 3h4l2 5-2.5 1.5a11 11 0 0 0 6 6L16 13l5 2v4a2 2 0 0 1-2 2A16 16 0 0 1 3 5a2 2 0 0 1 2-2z"/></svg>
    CALL US NOW - <b>555-014-2297</b>
  </div>
  <div class="abs social-top"><span></span><span></span><span></span></div>
  <span class="abs nav active" style="left:110px">HOME</span>
  <span class="abs nav" style="left:204px">ABOUT</span>
  <span class="abs nav" style="left:304px">SERVICES</span>
  <span class="abs nav" style="left:428px">RESOURCE</span>
  <div class="abs brand"><div class="mark"></div><div class="name">VORMESH</div></div>
  <span class="abs nav" style="left:695px">BUSINESS</span>
  <span class="abs nav" style="left:820px">COMMUNITY</span>
  <span class="abs nav" style="left:964px">CONTACT</span>
  <svg class="abs" style="left:1068px;top:78px" width="20" height="20" viewBox="0 0 24 24" fill="none" stroke="#fff" stroke-width="2"><circle cx="10" cy="10" r="7"/><path d="M15 15l6 6"/></svg>
</header>

<svg class="abs hero" width="1200" height="710" viewBox="0 0 1200 710">
  <defs>
    <linearGradient id="heroFill" x1="0" y1="0" x2="0" y2="1">
      <stop offset="0" stop-color="#6f7c88"/>
      <stop offset=".5" stop-color="#55595e"/>
      <stop offset="1" stop-color="#8d8f91"/>
    </linearGradient>
  </defs>
  <polygon role="img" aria-label="Stacked salvage cars in a scrap yard rack" points="0,0 1200,0 1200,555 300,684 0,564" fill="url(#heroFill)"/>
  <rect width="1200" height="710" fill="rgba(0,0,0,.18)" style="clip-path:polygon(0 0,100% 0,100% 78%,25% 96%,0 79%)"/>
  <polyline points="0,574 300,698 1200,572" fill="none" stroke="#8cc63f" stroke-width="4"/>
</svg>
<div class="abs center hero-title">VORMESH</div>
<div class="abs center hero-sub">Nemo enim ipsam voluptatem quia voluptas sit aspernatur aut odit<br>aut fugit, sed quia consequuntur magni</div>
<div class="abs btn" style="left:509px;top:483px;width:162px;height:46px">GET STARETD</div>
<div class="abs dot" style="left:261px;top:731px"></div>
<div class="abs dot" style="left:289px;top:731px"></div>
<div class="abs dot on" style="left:318px;top:731px"></div>
<div class="abs dot" style="left:346px;top:731px"></div>

<!-- about -->
<div class="abs photo" role="img" aria-label="Pile of scrap metal under a blue sky" style="left:112px;top:934px;width:375px;height:434px;background:linear-gradient(180deg,#b9d1e8 0%,#9fb6c8 22%,#6e6f72 45%,#3f4043 100%)"></div>
<div class="abs frame"></div>
<div class="abs h2" style="left:523px;top:990px">ABOUT US</div>
<p class="abs para" style="left:526px;top:1052px;width:524px">Nemo enim ipsam voluptatem quia voluptas sit aspernatur aut odit aut fugit, sed quia consequuntur magni dolores eos qui ratione voluptatem sequi nesciunt. Neque porro quisquam est, qui dolorem ipsum quia dolor sit amet, consectetur, adipisci velit, sed quia non numquam eius modi tempora incidunt ut labore et dolore magnam aliquam quaerat voluptatem. totam rem aperiam,</p>
<div class="abs btn" style="left:521px;top:1272px;width:154px;height:50px">READ MORE</div>

<!-- services -->
<div class="abs band-dark" style="top:1471px;height:129px"></div>
<div class="abs center band-title" style="top:1510px">OUR SERVICES</div>
<svg class="abs chev" style="left:76px;top:1856px" viewBox="0 0 20 30" fill="none" stroke="#888" stroke-width="2"><path d="M14 4L4 15l10 11"/></svg>
<svg class="abs chev" style="left:1107px;top:1856px" viewBox="0 0 20 30" fill="none" stroke="#888" stroke-width="2"><path d="M6 4l10 11-10 11"/></svg>

<article class="abs service" style="left:112px">
  <div class="img" role="img" aria-label="Crane grabbing scrap metal at a recycling yard" style="background:linear-gradient(180deg,#7fb1dd 0%,#a9c9e4 45%,#8a6b4e 75%,#5b4a3d 100%)"></div>
  <h3>METAL RECYCLING</h3>
  <p>Nemo enim ipsam voluptatem &nbsp;aspernatur aut odit aut fugit, sed quia consequuntur magni ipsam voluptatem</p>
  <a>READ MORE</a>
</article>
<article class="abs service" style="left:442px">
  <div class="img" role="img" aria-label="Damaged front of a wrecked car" style="background:linear-gradient(135deg,#3a4556 0%,#8d949c 50%,#c9ccd0 100%)"></div>
  <h3>HEADLIGHT AND TAIL LIGHT</h3>
  <p>Nemo enim ipsam voluptatem &nbsp;aspernatur aut odit aut fugit, sed quia consequuntur magni ipsam voluptatem</p>
  <a>READ MORE</a>
</article>
<article class="abs service" style="left:770px">
  <div class="img" role="img" aria-label="Used cars parked in a garage" style="background:linear-gradient(180deg,#9aa0a6 0%,#d3d5d7 45%,#4d5157 100%)"></div>
  <h3>DELIVERY</h3>
  <p>Nemo enim ipsam voluptatem &nbsp;aspernatur aut odit aut fugit, sed quia consequuntur magni ipsam voluptatem</p>
  <a>READ MORE</a>
</article>

<!-- how it works -->
<div class="abs h2" style="left:112px;top:2180px">HOW IT WORKS</div>
<p class="abs para" style="left:112px;top:2239px;width:480px">Nemo enim ipsam voluptatem quia voluptas sit aspernatur aut odit aut fugit, sed quia consequuntur magni dolores eos qui ratione voluptatem sequi nesciunt. Neque porro quisquam est, qui dolorem ipsum quia dolor sit amet, consectetur, adipisci velit, sed quia non numquam eius modi tempora incidunt ut labore et dolore magnam aliquam quaerat voluptatem. totam rem aperiam,</p>
<div class="abs btn" style="left:112px;top:2468px;width:153px;height:50px">WATCH VIDEO</div>
<div class="abs" role="img" aria-label="Old cars parked beside a workshop, video preview" style="left:630px;top:2191px;width:458px;height:336px;background:linear-gradient(120deg,#b9b7b1 0%,#8f8f92 40%,#3b4a78 60%,#c46a2f 85%,#d9d6cf 100%);box-shadow:0 2px 8px rgba(0,0,0,.2)"></div>
<svg class="abs" style="left:823px;top:2325px" width="72" height="72" viewBox="0 0 72 72"><circle cx="36" cy="36" r="36" fill="#8cc63f"/><path d="M29 24l20 12-20 12z" fill="#fff"/></svg>

<!-- benefits -->
<div class="abs benefits" role="img" aria-label="Close-up of old engine gears and machine parts" style="background:radial-gradient(circle at 20% 40%,#4a4440 0%,#2c2a29 45%,#1f1e1e 100%)"></div>
<div class="abs center band-title" style="top:2778px">VEHICLE RECYCLING BENEFITS</div>
<p class="abs benefits-text">Nemo enim ipsam voluptatem quia voluptas sit aspernatur aut odit aut fugit, sed quia consequuntur magni dolores eos qui ratione voluptatem sequi nesciunt. Neque porro quisquam est, qui dolorem ipsum quia dolor sit amet, consectetur, adipisci velit, sed quia non numquam eius modi tempora incidunt ut labore et dolore magnam aliquam quaerat voluptatem. totam rem aperiam,</p>

<!-- blogs -->
<div class="abs center h2" style="top:3194px">LATEST BLOGS</div>
<p class="abs center" style="top:3250px;font-size:14px;line-height:26px;color:var(--muted)">Nemo enim ipsam voluptatem quia voluptas sit aspernatur aut odit aut fugit,<br>sed quia consequuntur magni dolores</p>
<svg class="abs chev" style="left:82px;top:3444px" viewBox="0 0 20 30" fill="none" stroke="#666" stroke-width="2"><path d="M14 4L4 15l10 11"/></svg>
<svg class="abs chev" style="left:1090px;top:3444px" viewBox="0 0 20 30" fill="none" stroke="#666" stroke-width="2"><path d="M6 4l10 11-10 11"/></svg>

<article class="abs blog" style="left:111px" role="img" aria-label="Blue skip truck in a depot">
  <div class="abs" style="inset:0;background:linear-gradient(160deg,#c7cbd1 0%,#6f7c9a 45%,#3a3f52 75%,#5a5650 100%)"></div>
  <div class="cap" style="top:160px">LOREM IPSUM DOLOR SIT AMET,<br>CONSECTETUR<br><span class="date">14-05-2020</span></div>
</article>
<article class="abs blog" style="left:440px" role="img" aria-label="Stack of used tyres">
  <div class="abs" style="inset:0;background:linear-gradient(180deg,#4a4a4a 0%,#262626 60%,#2e3a24 100%)"></div>
  <div class="cap" style="top:90px">LOREM IPSUM DOLOR SIT AMET,<br>CONSECTETUR<br><span class="date">14-05-2020</span></div>
  <div class="cap more" style="top:206px">READ MORE &nbsp;&#9702;</div>
</article>
<article class="abs blog" style="left:770px" role="img" aria-label="Crane lifting a scrapped white car">
  <div class="abs" style="inset:0;background:linear-gradient(180deg,#8fb3d8 0%,#b6c8d8 45%,#7d7f82 75%,#5c5a58 100%)"></div>
  <div class="cap" style="top:160px">LOREM IPSUM DOLOR SIT AMET,<br>CONSECTETUR<br><span class="date">14-05-2020</span></div>
</article>

<!-- contact -->
<div class="abs band-green"></div>
<div class="abs band-title" style="left:0;width:1164px;text-align:center;top:3733px">CONTACT US</div>
<div class="abs field" style="left:227px;top:3880px;width:365px;height:52px">First Name</div>
<div class="abs field" style="left:608px;top:3880px;width:365px;height:52px">Last Name</div>
<div class="abs field" style="left:227px;top:3946px;width:365px;height:52px">Email</div>
<div class="abs field" style="left:608px;top:3946px;width:365px;height:52px">Phone</div>
<div class="abs field" style="left:227px;top:4014px;width:746px;height:153px">Message</div>
<div class="abs" style="left:241px;top:4202px;font-size:14px;color:#777">Forgot your password?</div>
<div class="abs send">SEND</div>

<!-- footer -->
<footer class="abs site-footer"></footer>
<div class="abs f-head" style="left:112px">QUICK LINKS</div>
<ul class="abs f-list" style="left:112px"><li>Home</li><li>About Us</li><li>Services</li><li>Resource</li><li>Community</li><li>Contact</li></ul>
<div class="abs f-head" style="left:326px">ABOUT</div>
<ul class="abs f-list" style="left:326px"><li>Team</li><li>News</li><li>Terms &amp; Condition</li><li>Privacy/Policy</li></ul>
<div class="abs f-head" style="left:555px">CONTACT US</div>
<div class="abs f-icon" style="left:554px;top:4444px"><svg width="18" height="18" viewBox="0 0 24 24" fill="none" stroke="#fff" stroke-width="1.8"><path d="M12 22s7-7 7-12a7 7 0 0 0-14 0c0 5 7 12 7 12z"/><circle cx="12" cy="10" r="2.5"/></svg></div>
<div class="abs f-txt" style="left:612px;top:4446px">Nemo enim ipsam voluptatem<br>quia voluptas sit</div>
<div class="abs f-icon" style="left:554px;top:4530px"><svg width="18" height="18" viewBox="0 0 24 24" fill="none" stroke="#fff" stroke-width="1.8"><path d="M5 3h4l2 5-2.5 1.5a11 11 0 0 0 6 6L16 13l5 2v4a2 2 0 0 1-2 2A16 16 0 0 1 3 5a2 2 0 0 1 2-2z"/></svg></div>
<div class="abs f-txt" style="left:612px;top:4537px">555-014-2297</div>
<div class="abs f-icon" style="left:554px;top:4605px"><svg width="18" height="18" viewBox="0 0 24 24" fill="none" stroke="#fff" stroke-width="1.8"><rect x="3" y="5" width="18" height="14" rx="2"/><path d="M3 7l9 6 9-6"/></svg></div>
<div class="abs f-txt" style="left:612px;top:4612px">info@vormesh.com</div>
<div class="abs f-head" style="left:947px">CONNECT WITH US</div>
<div class="abs s-row" style="top:4451px"><span></span>Friendloop</div>
<div class="abs s-row" style="top:4503px"><span></span>Snapfold</div>
<div class="abs s-row" style="top:4555px"><span></span>Chirpline</div>
<div class="abs s-row" style="top:4606px"><span></span>Workweave</div>
<div class="abs rule"></div>
<div class="abs center copy">© 2020 All Rights Reserved</div>

</body>
</html>
```